PHARMACY ASSISTANTS STUDY COURSE BROCHURE

We need a 4 page, A4, 4 colour brochure.
The market is pharmacy assistants mid 20's and up who are looking at expanding their Pharmacy knowledge and wanting to study more.

The brief is attached - 15:09:23

We need to make our 4 pager modern in regards to layout and colours.

For the front use the pixvault image. And for the pack the other image - 583

The course fees chart also needs to be laid out better than the original one. Text has been retyped out

The course chart - the copy has been typed out as well

Various logos attached too.

Corporate guidelines attached for typefaces.

FILES ARE:
12-09-20 DRAF7LUX = image for back
pixvault image = for front
15:09:23 = brief
15:09:24 = typed up certificate course text
Course fees = typed up fees text
A4 Bi-fold - reference to last brochure
Nationally Recognised - logo for back
KTR logo - Circle logo

```html
<!DOCTYPE html>
<html lang="en">
<head>
<meta charset="utf-8">
<title>Pharmacy Assistant Training Brochure</title>
<link href="https://fonts.googleapis.com/css2?family=Open+Sans:wght@400;600;700;800&display=swap" rel="stylesheet">
<style>
:root{
  --navy:#1c3768;
  --navy-deep:#142a52;
  --yellow:#f4c21b;
  --ink:#33384a;
  --muted:#6b7183;
  --line:#d6dae4;
  --paper:#ffffff;
  --bg:#e9ebef;
}
*{box-sizing:border-box;margin:0;padding:0}
html,body{width:849px;height:1200px;overflow:hidden;background:var(--bg);font-family:"Open Sans",Arial,sans-serif;color:var(--ink)}
.page{position:absolute;background:var(--paper);overflow:hidden}
.back{left:0;top:0;width:424px;height:460px}
.front{left:425px;top:0;width:424px;height:460px}
.inside-left{left:0;top:480px;width:424px;height:720px}
.inside-right{left:425px;top:480px;width:424px;height:720px}
.photo{position:absolute}
.brand-name{font-weight:700;color:var(--navy);font-size:10px;line-height:1.2;white-space:nowrap}
p{font-size:5.4px;line-height:1.5}
/* back */
.back .photo{left:150px;top:0;width:274px;height:205px;background:linear-gradient(160deg,#f2f4f7,#d9dde4 60%,#c6ccd6)}
.back .lead{position:absolute;left:40px;top:190px;width:170px;font-size:11px;font-weight:700;color:var(--navy);line-height:1.3}
.rpl-band{position:absolute;left:0;top:262px;width:424px;height:36px;background:var(--navy);color:#fff;font-size:9px;font-weight:600;padding:8px 40px;line-height:1.3}
.back .brand-name{position:absolute;left:40px;top:322px}
.contacts{position:absolute;left:40px;top:350px;display:flex;gap:40px}
.contacts p{font-size:5.5px;color:var(--ink)}
.back .legal{position:absolute;left:40px;top:392px;width:300px;color:var(--muted);font-size:4.5px}
/* front */
.front .photo{left:0;top:0;width:424px;height:262px;background:linear-gradient(135deg,#e3e8ee,#c9d3de 55%,#aebccb)}
.front .brand-name{position:absolute;right:20px;top:18px;background:#fff;padding:8px 10px}
.front h1{position:absolute;left:180px;top:280px;width:230px;font-size:23px;font-weight:700;color:var(--navy);line-height:1.1}
.front .sub{position:absolute;left:180px;top:336px;width:220px;font-size:8px;line-height:1.4;color:var(--ink)}
.front .sub b{color:var(--navy)}
.front .legal{position:absolute;left:180px;top:412px;width:220px;color:var(--muted);font-size:4.5px}
/* inside left */
.side{position:absolute;left:0;top:0;width:140px;height:720px;background:var(--navy);padding:60px 16px 0;color:#fff}
.side h2{font-size:20px;font-weight:800;color:var(--yellow);line-height:1.1;margin-bottom:14px}
.side p{color:#e4e9f3;margin-bottom:8px;font-size:5.8px}
.side p b{color:var(--yellow)}
.certs{position:absolute;left:160px;top:60px;width:240px}
.certs h3{font-size:8px;font-weight:700;color:var(--navy);margin:16px 0 5px}
.certs h3:first-child{margin-top:12px}
.certs h4{font-size:6px;font-weight:700;color:var(--ink);margin:6px 0 2px}
.certs p{font-size:5.8px}
.certs ul{list-style:none;margin:2px 0 4px}
.certs li{font-size:5.8px;line-height:1.6;padding-left:7px;position:relative}
.certs li::before{content:"";position:absolute;left:0;top:3.5px;width:3px;height:3px;background:var(--yellow)}
/* inside right */
.fees{position:absolute;left:24px;top:60px;width:376px}
.fees h2{font-size:20px;font-weight:800;color:var(--navy);margin-bottom:8px}
.fee-grid{display:flex;gap:8px;margin-top:12px}
.fee-col{flex:1;border:1px solid var(--line)}
.fee-head{background:var(--navy);color:#fff;font-size:7px;font-weight:700;padding:5px 6px;display:flex;justify-content:space-between}
.fee-head span{color:var(--yellow)}
.fee-sub{background:#eef1f6;font-size:5.4px;font-weight:700;color:var(--navy);padding:4px 6px}
.fee-row{display:flex;justify-content:space-between;font-size:5.2px;padding:4px 6px;border-top:1px solid var(--line);line-height:1.4}
.fee-row b{color:var(--navy)}
.fee-note{font-size:4.8px;color:var(--muted);margin-top:10px;line-height:1.5}
.payment{position:absolute;left:24px;top:520px;width:376px;background:var(--navy);color:#fff;padding:12px 14px;display:flex;gap:14px}
.payment h3{font-size:8px;color:var(--yellow);font-weight:700;margin-bottom:4px}
.payment p{color:#e4e9f3}
.payment div{flex:1}
</style>
</head>
<body>

<section class="page back">
  <div class="photo" role="img" aria-label="Photo of a smiling pharmacy assistant"></div>
  <p class="lead">Did you know that your prior knowledge and experience gained on the job may work towards gaining a nationally recognised qualification?</p>
  <div class="rpl-band">If you've been working in pharmacy for a while, make sure you ask about 'Recognition of Prior Learning' (or 'RPL').</div>
  <div class="brand-name">Pharmacy Circle</div>
  <div class="contacts">
    <p>48 Harbour Row<br>Eastfield NSW 2190</p>
    <p>Ph 02 9000 4412<br>Fax 02 9000 4413</p>
    <p>training@pharmacycircle.org<br>pharmacycircle.org</p>
  </div>
  <p class="legal">The Pharmacy Circle NSW Branch is a registered training organisation. Course details and fees are correct at the time of printing and may change without notice.</p>
</section>

<section class="page front">
  <div class="photo" role="img" aria-label="Photo of a pharmacy assistant at a pharmacy counter"></div>
  <div class="brand-name">Pharmacy Circle</div>
  <h1>Pharmacy Assistant Training</h1>
  <p class="sub">Give yourself a head start with the NSW <b>Skilled Futures</b> training program.</p>
  <p class="legal">This training program is subsidised by the NSW Government. Eligibility criteria apply to all enrolments.</p>
</section>

<section class="page inside-left">
  <div class="side">
    <h2>Skilled Futures</h2>
    <p>From January, NSW Government funding for vocational training will be delivered through <b>Skilled Futures</b>, giving learners more choice in where and how they study.</p>
    <p>The Skilled Futures program helps eligible people gain the skills they need for a job and career, with subsidised places in qualifications on the state skills list.</p>
    <p>The Pharmacy Circle is an approved training provider and can help you check your eligibility, choose a course and plan your study around your working week.</p>
    <p>Speak to our training team today to find out how you can get started.</p>
  </div>
  <div class="certs">
    <h3>Certificate II Community Pharmacy (SIR20112)</h3>
    <h4>Who should do this course?</h4>
    <p>This course suits new pharmacy assistants who are starting out in retail pharmacy.</p>
    <h4>What will you learn?</h4>
    <ul>
      <li>Working effectively in a community pharmacy team</li>
      <li>Providing quality customer service</li>
      <li>Merchandising and stock handling</li>
      <li>Safe work practices in the pharmacy</li>
    </ul>
    <h3>Certificate III Community Pharmacy (SIR30112)</h3>
    <h4>Who should do this course?</h4>
    <p>This course suits pharmacy assistants with some experience who want to build product knowledge.</p>
    <h4>What will you learn?</h4>
    <ul>
      <li>Supplying non-prescription medicines and products</li>
      <li>Assisting customers with health and wellbeing needs</li>
      <li>Recommending skin care and vitamin products</li>
      <li>Working under pharmacist supervision</li>
      <li>Handling customer complaints</li>
    </ul>
    <h3>Certificate IV Community Pharmacy (SIR40112)</h3>
    <h4>Who should do this course?</h4>
    <p>This course suits experienced assistants moving into senior or supervisory roles.</p>
    <h4>What will you learn?</h4>
    <ul>
      <li>Leading and supporting a pharmacy team</li>
      <li>Managing stock and retail operations</li>
      <li>Advanced product and health knowledge</li>
      <li>Coaching and training other staff</li>
    </ul>
  </div>
</section>

<section class="page inside-right">
  <div class="fees">
    <h2>Course Fees</h2>
    <p>The fees below are indicative and depend on your eligibility under the Skilled Futures program. Concession and exemption rates apply to eligible students. Please contact our team for a personalised quote before you enrol.</p>
    <div class="fee-grid">
      <div class="fee-col">
        <div class="fee-head">CERTIFICATE II <span>SIR20112</span></div>
        <div class="fee-sub">Skilled Futures subsidised</div>
        <div class="fee-row"><span>Standard fee</span><b>$650</b></div>
        <div class="fee-row"><span>Concession fee</span><b>$160</b></div>
        <div class="fee-row"><span>Fee exempt</span><b>$0</b></div>
        <div class="fee-sub">Full fee (not eligible)</div>
        <div class="fee-row"><span>Course fee</span><b>$1,450</b></div>
        <div class="fee-row"><span>Resources</span><b>$120</b></div>
      </div>
      <div class="fee-col">
        <div class="fee-head">CERTIFICATE III <span>SIR30112</span></div>
        <div class="fee-sub">Skilled Futures subsidised</div>
        <div class="fee-row"><span>Standard fee</span><b>$980</b></div>
        <div class="fee-row"><span>Concession fee</span><b>$240</b></div>
        <div class="fee-row"><span>Fee exempt</span><b>$0</b></div>
        <div class="fee-sub">Full fee (not eligible)</div>
        <div class="fee-row"><span>Course fee</span><b>$2,150</b></div>
        <div class="fee-row"><span>Resources</span><b>$150</b></div>
      </div>
      <div class="fee-col">
        <div class="fee-head">CERTIFICATE IV <span>SIR40112</span></div>
        <div class="fee-sub">Skilled Futures subsidised</div>
        <div class="fee-row"><span>Standard fee</span><b>$1,260</b></div>
        <div class="fee-row"><span>Concession fee</span><b>$240</b></div>
        <div class="fee-row"><span>Fee exempt</span><b>$0</b></div>
        <div class="fee-sub">Full fee (not eligible)</div>
        <div class="fee-row"><span>Course fee</span><b>$2,800</b></div>
        <div class="fee-row"><span>Resources</span><b>$180</b></div>
      </div>
    </div>
    <p class="fee-note">All fees are GST free. Fees are reviewed each year and may change. Payment is due before the course start date unless a payment plan has been agreed in writing.</p>
  </div>
  <div class="payment">
    <div>
      <h3>Pharmacy Circle NSW Branch Payment Plan Options</h3>
      <p>Spread the cost of your course with a simple payment plan. Pay a deposit on enrolment and the balance in equal monthly instalments across your study period.</p>
    </div>
    <div>
      <h3>Need more information?</h3>
      <p>Call our training team on 02 9000 4412 or email training@pharmacycircle.org to discuss your options and enrol.</p>
    </div>
  </div>
</section>

</body>
</html>
```